Financial Planning Business needs a business card design

We need a business card design that is for a new financial planning business based in Australia. We provide financial planning advice such as retirement planning, wealth creation, asset protection.

Attached is the logo design. On the front side of the business card needs to incorporate the following:
- adviser name
- adviser title (ie Managing Director)
- address
- phone number
- email
- website address

Ideally it should also have the business name and logo

On the back of the card I would like this to be black in colour with the business name and logo

I have been advised the font is "Cinzel" (regular and bold)

Industry/Entity Type

Financial

Requirements
Must have
• Logo and business name

Format to have as follows:
Ben xxxxxxxx
Managing Director / Senior Financial Adviser
address
phone email
website

```html
<!DOCTYPE html>
<html lang="en">
<head>
<meta charset="utf-8">
<title>Keystone Wealth Planning – Business Card</title>
<link rel="stylesheet" href="https://fonts.googleapis.com/css2?family=Cinzel:wght@400;700&family=Montserrat:wght@400;700&display=swap">
<style>
  :root {
    --stage: #0e1112;
    --card-white: #ffffff;
    --brand-blue: #009ccf;
    --brand-blue-deep: #0090c6;
    --brand-grey: #a3a3a3;
    --text-light: #ffffff;
  }
  * { margin: 0; padding: 0; box-sizing: border-box; }
  html, body {
    width: 1200px;
    height: 750px;
    overflow: hidden;
    background: var(--stage);
  }
  .card {
    position: absolute;
    left: 200px;
    top: 136px;
    width: 800px;
    height: 478px;
    background: var(--card-white);
    overflow: hidden;
  }
  .brand {
    position: absolute;
    left: 170px;
    top: 54px;
    height: 107px;
    display: flex;
    align-items: center;
    gap: 20px;
  }
  .brand-mark {
    width: 92px;
    height: 92px;
    background: var(--brand-grey);
  }
  .brand-name {
    font-family: "Cinzel", serif;
    font-weight: 400;
    color: var(--brand-blue);
    line-height: 1;
  }
  .brand-name .primary {
    display: block;
    font-size: 66px;
    letter-spacing: 1px;
  }
  .brand-name .secondary {
    display: block;
    font-size: 29px;
    letter-spacing: 1px;
    margin-top: 4px;
  }
  .details-band {
    position: absolute;
    left: 0;
    top: 207px;
    width: 800px;
    height: 271px;
    background: var(--brand-blue);
  }
  .details-band svg {
    position: absolute;
    left: 0;
    top: 0;
  }
  .contact {
    position: absolute;
    left: 0;
    top: 0;
    width: 800px;
    text-align: center;
    color: var(--text-light);
    font-family: "Montserrat", sans-serif;
  }
  .contact .adviser-name {
    position: absolute;
    left: 0; width: 800px;
    top: 43px;
    font-family: "Cinzel", serif;
    font-weight: 400;
    font-size: 29px;
    letter-spacing: 1px;
  }
  .contact .adviser-title {
    position: absolute;
    left: 0; width: 800px;
    top: 93px;
    font-weight: 700;
    font-size: 16px;
    letter-spacing: 0.5px;
  }
  .contact .line {
    position: absolute;
    left: 0; width: 800px;
    font-size: 14.5px;
    letter-spacing: 0.3px;
  }
  .contact .line-1 { top: 125px; }
  .contact .line-2 { top: 151px; }
  .contact .line-3 { top: 177px; }
  .contact .line-4 { top: 203px; }
  .divider { margin: 0 8px; }
</style>
</head>
<body>
  <main class="card">
    <header class="brand">
      <div class="brand-mark"></div>
      <div class="brand-name">
        <span class="primary">KEYSTONE</span>
        <span class="secondary">WEALTH PLANNING</span>
      </div>
    </header>
    <section class="details-band">
      <svg width="800" height="271" viewBox="0 0 800 271" aria-hidden="true">
        <polygon points="400,42 800,271 0,271" fill="var(--brand-blue-deep)"/>
      </svg>
      <div class="contact">
        <p class="adviser-name">BEN SURNAME</p>
        <p class="adviser-title">Managing Director</p>
        <p class="line line-1">Address line. address line address line</p>
        <p class="line line-2">Address line. address line address</p>
        <p class="line line-3">123 555-0142<span class="divider">I</span>email@keystonewealth.com</p>
        <p class="line line-4">www.keystonewealth.com</p>
      </div>
    </section>
  </main>
</body>
</html>
```